Ecommerce Website For Printing Company

Quillbarn.com are a print, design and signage company who sell flyers, business cards, posters, brochures and more to customers in the UK.

Our website is outdated and requires a new design using current web styling and mobile functionality.

We require the following pages to be designed;
- Home Page
- Price Page
- Portfolio Page
- Blog
- Content Page

Our competitors in the printing industry are www.tavenink.com, www.marlowpress.co.uk, brightquire.co.uk, www.leafcrate.co.uk

We require the website to give a professional image as well as be easy for customers to navigate, understand and find prices.

Target Market(s)

Businesses

Industry/Entity Type

Printing

Number of Pages Required

4 page

Font styles to use
Sans Serif

Colors
33a6d7

Requirements
Must have
• Popular products, latest news/blog, sales from portfolio, newsletter sign up, footer

```html
<!DOCTYPE html>
<html lang="en">
<head>
<meta charset="utf-8">
<title>Quillbarn.com – Print, Design &amp; Signage</title>
<link href="https://fonts.googleapis.com/css2?family=Lato:wght@300;400;700;900&display=swap" rel="stylesheet">
<style>
:root{
  --brand:#33a6d7;
  --ink:#333638;
  --muted:#7d8286;
  --line:#e3e5e7;
  --pale:#f4f5f6;
  --dark:#2f3133;
  --darker:#25272a;
  --white:#ffffff;
}
*{box-sizing:border-box;margin:0;padding:0}
html,body{width:1200px;height:2460px;overflow:hidden}
body{font-family:"Lato",sans-serif;color:var(--ink);background:var(--white);font-size:14px;position:relative}
a{color:inherit;text-decoration:none}

.topbar{height:28px;background:var(--dark);color:#c9ccd0;font-size:11px;display:flex;align-items:center;justify-content:space-between;padding:0 40px}
.topbar .links{display:flex;gap:22px}
.topbar .phone{display:flex;align-items:center;gap:6px}

.header{height:110px;display:flex;align-items:center;justify-content:center;position:relative;border-bottom:1px solid var(--line)}
.logo{display:flex;align-items:center;gap:12px;color:var(--brand);font-weight:900;font-size:46px;letter-spacing:-1px}
.logo .mark{width:30px;height:30px;background:var(--brand)}
.header .tools{position:absolute;right:40px;display:flex;gap:10px;align-items:center}
.search{width:150px;height:30px;border:1px solid var(--line);font-size:11px;color:var(--muted);display:flex;align-items:center;padding:0 10px}
.cart{height:30px;padding:0 12px;border:1px solid var(--line);display:flex;align-items:center;font-size:11px;color:var(--muted);gap:6px}

.nav{height:48px;display:flex;align-items:center;justify-content:center;border-bottom:1px solid var(--line)}
.nav a{padding:0 20px;font-size:12px;font-weight:700;letter-spacing:.5px;height:48px;display:flex;align-items:center}
.nav a.active{color:var(--brand)}

.hero{position:relative;height:410px;background:linear-gradient(180deg,#b7793f 0%,#9a5e2c 55%,#7d4820 100%);overflow:hidden}
.hero .art{position:absolute;left:420px;top:30px;width:560px;height:350px;background:linear-gradient(135deg,#2b3440,#1c6f95 45%,#e8ecef 70%,#f3c441);transform:rotate(-6deg);opacity:.9;border-radius:4px}
.hero .copy{position:absolute;left:150px;top:120px;color:var(--white)}
.hero h1{font-size:40px;font-weight:900;line-height:1.05;letter-spacing:.5px}
.hero p{font-size:12px;margin:14px 0 18px;width:210px;line-height:1.5;opacity:.9}
.btn{display:inline-flex;align-items:center;justify-content:center;background:var(--brand);color:var(--white);font-size:12px;font-weight:700;letter-spacing:1px;height:36px;padding:0 20px;white-space:nowrap}
.hero .arrow{position:absolute;top:180px;width:34px;height:50px;background:rgba(0,0,0,.35);display:flex;align-items:center;justify-content:center}
.hero .arrow.left{left:0}.hero .arrow.right{right:0}

.tabs{display:flex;width:1040px;margin:84px auto 0}
.tabs div{flex:1;height:46px;border:1px solid var(--line);background:var(--pale);display:flex;align-items:center;justify-content:center;font-size:17px;font-weight:300;letter-spacing:1px;color:var(--muted)}
.tabs div.on{background:var(--white);border-bottom-color:var(--white)}

.section-title{text-align:center;font-size:22px;font-weight:900;letter-spacing:1px;line-height:30px;margin:38px 0 26px}
.section-title span{display:inline-flex;align-items:center;gap:18px}
.section-title span::before,.section-title span::after{content:"";width:60px;height:1px;background:var(--line)}
.section-title.blog-title{margin:60px 0 52px}

.products{display:flex;gap:40px;width:1040px;margin:0 auto}
.product{flex:1;border:1px solid var(--line)}
.product .img{height:300px}
.product .img.p1{background:linear-gradient(160deg,#fafafa 30%,#d9eef8 60%,#f7f7f7)}
.product .img.p2{background:linear-gradient(160deg,#fff 20%,#3aa6d4 45%,#f2b13b 70%,#fff)}
.product .img.p3{background:linear-gradient(160deg,#fff 20%,#e14f4f 45%,#4aa8d8 65%,#fff)}
.product .img.p4{background:linear-gradient(160deg,#fff 25%,#eef1f3 55%,#fff)}
.product .info{display:flex;justify-content:space-between;align-items:center;padding:14px;border-top:1px solid var(--line);height:62px}
.product h3{font-size:12px;font-weight:700;letter-spacing:.5px}
.product .price{font-size:11px;color:var(--muted);margin-top:4px}
.product .price b{color:var(--brand)}
.product .add{width:34px;height:34px;background:var(--brand);display:flex;align-items:center;justify-content:center}

.care{margin-top:84px;height:328px;background:var(--brand);color:var(--white);position:relative}
.care h2{position:absolute;left:80px;top:40px;font-size:34px;font-weight:900;line-height:1.05;letter-spacing:.5px}
.care .showcase{position:absolute;left:80px;top:130px;width:520px;height:170px;background:linear-gradient(120deg,#f1f3f5 0%,#d9e3ea 40%,#f3c441 70%,#d94f4f 100%);border-radius:3px}
.care .text{position:absolute;left:650px;top:44px;width:470px;font-size:12px;line-height:1.65}
.care .text p+p{margin-top:10px}
.care .actions{position:absolute;left:720px;top:250px;display:flex;gap:14px}
.care .actions .btn{background:var(--darker)}

.newsletter{height:128px;background:var(--dark);display:flex;align-items:center;justify-content:space-between;padding:0 80px}
.newsletter h2{color:var(--white);font-size:22px;font-weight:900;letter-spacing:.5px}
.newsletter form{display:flex;gap:12px}
.field{width:200px;height:36px;background:var(--white);font-size:12px;color:var(--muted);display:flex;align-items:center;padding:0 12px}

.blog{display:flex;gap:40px;width:1040px;margin:0 auto}
.post{flex:1;border-top:2px solid var(--brand);padding-top:16px}
.post .date{font-size:10px;color:var(--muted);letter-spacing:1px}
.post h3{font-size:17px;font-weight:900;margin:10px 0 12px}
.post p{font-size:12px;line-height:1.7;color:var(--muted)}
.post .more{display:inline-block;margin-top:14px;font-size:12px;color:var(--brand);font-weight:700}

.footer{position:absolute;left:0;top:2180px;width:1200px;height:232px;background:var(--dark);color:#b9bdc1;padding:32px 80px 0;display:flex;gap:40px}
.footer .col{flex:1}
.footer h4{color:var(--white);font-size:14px;font-weight:900;margin-bottom:14px;padding-bottom:10px;border-bottom:1px solid #45484b}
.footer li{list-style:none;font-size:12px;line-height:2}
.social{display:flex;gap:8px;margin-top:12px}
.social span{width:26px;height:26px;border-radius:50%;background:var(--brand)}
.bottombar{position:absolute;left:0;top:2412px;width:1200px;height:48px;background:var(--darker);color:#8d9195;font-size:11px;display:flex;align-items:center;justify-content:space-between;padding:0 80px}
.cards{display:flex;gap:6px}
.cards span{width:32px;height:20px;background:#4a4d51;border-radius:2px}
</style>
</head>
<body>

<div class="topbar">
  <div class="phone">
    <svg width="11" height="11" viewBox="0 0 24 24" fill="#c9ccd0"><path d="M6.6 10.8a15 15 0 0 0 6.6 6.6l2.2-2.2c.3-.3.7-.4 1-.2 1.1.4 2.3.6 3.6.6.6 0 1 .4 1 1V20c0 .6-.4 1-1 1C10.6 21 3 13.4 3 4c0-.6.4-1 1-1h3.5c.6 0 1 .4 1 1 0 1.3.2 2.5.6 3.6.1.3 0 .7-.2 1z"/></svg>
    01632 960 480
  </div>
  <div class="links"><a>My Account</a><a>Checkout</a><a>Sign in</a><a>Create Account</a></div>
</div>

<header class="header">
  <a class="logo"><span class="mark"></span>Quillbarn.com</a>
  <div class="tools">
    <div class="search">Search…</div>
    <div class="cart">
      <svg width="14" height="14" viewBox="0 0 24 24" fill="none" stroke="#7d8286" stroke-width="2"><path d="M3 4h2l2.5 11h11L21 7H6.5"/><circle cx="9" cy="19" r="1.5"/><circle cx="17" cy="19" r="1.5"/></svg>
      £0.00
    </div>
  </div>
</header>

<nav class="nav">
  <a class="active">HOME</a><a>ABOUT US</a><a>GRAPHIC DESIGN</a><a>WEBSITE DESIGN</a><a>ARTWORK GUIDE</a><a>SAMPLE PACK</a><a>UPLOAD</a><a>TESTIMONIALS</a><a>BLOG</a><a>CONTACT US</a>
</nav>

<section class="hero" role="img" aria-label="Printed flyers and brochures spread across a wooden desk">
  <div class="art"></div>
  <div class="copy">
    <h1>SHEER MAGIC<br>IN PRINT</h1>
    <p>Choose the best in printing with Quillbarn.com</p>
    <a class="btn">LEARN MORE</a>
  </div>
  <div class="arrow left"><svg width="12" height="18" viewBox="0 0 12 18"><path d="M10 2 3 9l7 7" fill="none" stroke="#fff" stroke-width="2.5"/></svg></div>
  <div class="arrow right"><svg width="12" height="18" viewBox="0 0 12 18"><path d="M2 2l7 7-7 7" fill="none" stroke="#fff" stroke-width="2.5"/></svg></div>
</section>

<div class="tabs"><div>LARGE FORMAT</div><div class="on">POPULAR PRODUCTS</div><div>CANVAS PRINTS</div></div>

<h2 class="section-title"><span>FEATURED PRODUCTS</span></h2>

<div class="products">
  <div class="product"><div class="img p1" role="img" aria-label="Stack of printed business cards"></div>
    <div class="info"><div><h3>BUSINESS CARDS</h3><div class="price">from <b>£9.99</b></div></div>
    <span class="add"><svg width="16" height="16" viewBox="0 0 24 24" fill="none" stroke="#fff" stroke-width="2"><path d="M3 4h2l2.5 11h11L21 7H6.5"/><circle cx="9" cy="19" r="1.5"/><circle cx="17" cy="19" r="1.5"/></svg></span></div></div>
  <div class="product"><div class="img p2" role="img" aria-label="Folded leaflets in bright colours"></div>
    <div class="info"><div><h3>FOLDED LEAFLETS</h3><div class="price">from <b>£29.99</b></div></div>
    <span class="add"><svg width="16" height="16" viewBox="0 0 24 24" fill="none" stroke="#fff" stroke-width="2"><path d="M3 4h2l2.5 11h11L21 7H6.5"/><circle cx="9" cy="19" r="1.5"/><circle cx="17" cy="19" r="1.5"/></svg></span></div></div>
  <div class="product"><div class="img p3" role="img" aria-label="A6 flyers fanned out"></div>
    <div class="info"><div><h3>A6 FLYERS</h3><div class="price">from <b>£19.99</b></div></div>
    <span class="add"><svg width="16" height="16" viewBox="0 0 24 24" fill="none" stroke="#fff" stroke-width="2"><path d="M3 4h2l2.5 11h11L21 7H6.5"/><circle cx="9" cy="19" r="1.5"/><circle cx="17" cy="19" r="1.5"/></svg></span></div></div>
  <div class="product"><div class="img p4" role="img" aria-label="Printed letterhead sheets"></div>
    <div class="info"><div><h3>LETTERHEADS</h3><div class="price">from <b>£39.99</b></div></div>
    <span class="add"><svg width="16" height="16" viewBox="0 0 24 24" fill="none" stroke="#fff" stroke-width="2"><path d="M3 4h2l2.5 11h11L21 7H6.5"/><circle cx="9" cy="19" r="1.5"/><circle cx="17" cy="19" r="1.5"/></svg></span></div></div>
</div>

<section class="care">
  <h2>SMALL ENOUGH TO CARE.<br>BIG ENOUGH TO COPE.</h2>
  <div class="showcase" role="img" aria-label="Business cards, brochures and wedding stationery laid out together"></div>
  <div class="text">
    <p>Quillbarn.com is a small print and design company working on a national scale, serving businesses and organisations across the United Kingdom and Europe. As a company we are small enough to care and big enough to cope. We are an independent, owned family team who take pride in every job, from a handful of cards to large runs for trade clients.</p>
    <p>Our company is led by our philosophy: printing should be simple, fair and fast. We aim to offer quality products at honest prices and deliver them on time, every time, with friendly help whenever you need it.</p>
  </div>
  <div class="actions"><a class="btn">ORDER SAMPLE PACK</a><a class="btn">LEARN MORE</a></div>
</section>

<section class="newsletter">
  <h2>SIGN UP TO OUR NEWSLETTER</h2>
  <form><div class="field">Your Name</div><div class="field">Your Email</div><a class="btn">SUBSCRIBE</a></form>
</section>

<h2 class="section-title blog-title"><span>FROM THE BLOG</span></h2>

<div class="blog">
  <article class="post"><div class="date">12 MARCH 2015</div><h3>Standing Out</h3>
    <p>We have just completed a brand new print run for a local design studio. With bold colours and a clean layout, the cards really stand out on any desk and show how good paper stock can lift a simple idea.</p><a class="more">Read more ›</a></article>
  <article class="post"><div class="date">04 MARCH 2015</div><h3>Open Studios Ashbury</h3>
    <p>We are proud to support the Open Studios Ashbury event this spring with flyers, posters and banners. The team worked closely with the organisers to get every piece printed and delivered well ahead of opening night.</p><a class="more">Read more ›</a></article>
  <article class="post"><div class="date">22 FEBRUARY 2015</div><h3>Harwood Lane</h3>
    <p>This month we printed a full set of menus, cards and signs for Harwood Lane, a new café in town. Matching colours across each item gave the whole shop a fresh, joined up look that customers love.</p><a class="more">Read more ›</a></article>
</div>

<footer class="footer">
  <div class="col"><h4>Information</h4><ul><li>Home</li><li>About Us</li><li>Terms &amp; Conditions</li><li>Sitemap</li><li>Privacy Policy</li></ul></div>
  <div class="col"><h4>Support</h4><ul><li>FAQs</li><li>Specials</li><li>New products</li><li>Top sellers</li><li>Our stores</li></ul></div>
  <div class="col"><h4>Customer Services</h4><ul><li>Login / Register</li><li>Delivery Information</li><li>Payment Options</li><li>Returns Policy</li><li>Artwork Guide</li></ul></div>
  <div class="col"><h4>Contact Us</h4><ul><li>01632 960 480</li><li>hello@quillbarn.com</li></ul>
    <div class="social"><span></span><span></span><span></span><span></span></div></div>
</footer>

<div class="bottombar">
  <span>Copyright © 2015 Quillbarn.com. All rights reserved.</span>
  <div class="cards"><span></span><span></span><span></span><span></span></div>
</div>

</body>
</html>
```